Seed Oil Safety Card for Healthy Restaurant Dining

I am seeking a design for a physical card to communicate my wife's health-related dietary restriction regarding seed oils. This card will be given to restaurant waiters to ensure her meals are prepared without seed oils, as it is a health issue and not merely a preference.
My wife cannot eat any “seed oil” or “processed oil”, including:
- Vegetable oil
- Canola oil
- Soybean oil
- Sunflower oil
- Corn oil
- Cottonseed oil
- Safflower oil
- Peanut oil
- Sesame oil
Oils that are OK for her to consume:
- Butter (most preferable)
- Extra virgin olive oil
- Avocado oil
- Coconut oil
- Ghee
- Lard
- Any other animal-based fats
Key Design Requirements:
- Clarity and speed of communication: The card should be easily read and understood by waiters, even in low-light environments, emphasizing that it's a health concern.
- Avoid common misconceptions: Ensure the design doesn't imply common dietary preferences like "vegetarian" or "no butter." Animal fats and butter are actually preferable for her!
- Preferred term: Use "seed oils" as the term to describe what she cannot eat due to her health issue.
- Trace amounts are acceptable: Communicate that it's OK to use cookware that has previously been in contact with seed oils, but not to have seed oil as an ingredient. Please suggest a concise way to convey this.
- Card dimensions: Design should be 3.5” x 2.25” (standard credit-card size on cardlomex.example). Horizontal or vertical layouts are both fine, whichever makes the message clearer.
Design Suggestions:
- Utilize bold and easy-to-read typography to communicate the main message.
- Consider incorporating relevant icons or graphics that help convey the message without adding confusion.
- Use contrasting colors to enhance readability, especially in low-light situations.
- To communicate the “trace amounts OK” part, consider phrases such as:
- "Cross-contamination acceptable"
- “Used cookware OK, no ingredient use”
- “Separate cookware not necessary”
Thank you for your assistance in creating this essential card for my wife's health and safety when dining out!

```html
<!DOCTYPE html>
<html lang="en">
<head>
<meta charset="utf-8">
<title>Dietary Restriction Card</title>
<link rel="stylesheet" href="https://fonts.googleapis.com/css2?family=Archivo+Black&family=Arimo:ital,wght@0,400;0,700;1,400&display=swap">
<style>
  :root {
    --black: #000000;
    --white: #ffffff;
    --ink: #111111;
    --red: #c8000a;
    --red-dot: #d01c1c;
    --green: #3aa535;
    --yellow: #ffc90e;
    --yellow-ring: #ffffff;
  }
  * { margin: 0; padding: 0; box-sizing: border-box; }
  html, body { width: 1200px; height: 771px; overflow: hidden; background: var(--white); }
  .card {
    position: relative;
    width: 1200px; height: 771px;
    background: var(--white);
    color: var(--ink);
    font-family: "Arimo", Arial, sans-serif;
  }
  .card-header {
    position: absolute; left: 0; top: 0;
    width: 1200px; height: 139px;
    background: var(--black);
    display: flex; align-items: center; justify-content: center;
  }
  .card-title {
    font-family: "Archivo Black", "Arial Black", sans-serif;
    color: var(--white);
    font-size: 47px;
    letter-spacing: 1.5px;
    font-weight: 400;
  }
  .section-heading {
    position: absolute; left: 43px;
    font-family: "Archivo Black", "Arial Black", sans-serif;
    font-size: 31px; font-weight: 400;
    line-height: 1;
  }
  .heading-avoid { top: 165px; }
  .heading-ok { top: 408px; }
  .emph-red { color: var(--red); }
  .emph-green { color: var(--green); }
  .oil-list {
    position: absolute; list-style: none;
    font-size: 32px; line-height: 47.5px;
  }
  .oil-list li { position: relative; padding-left: 27px; }
  .oil-list li::before {
    content: ""; position: absolute; left: 2px; top: 21px;
    width: 8px; height: 8px; border-radius: 50%;
  }
  .avoid li::before { background: var(--red-dot); }
  .ok li::before { background: var(--green); }
  .avoid { top: 219px; }
  .ok { top: 461px; }
  .col-1 { left: 41px; }
  .col-2 { left: 310px; }
  .col-3 { left: 641px; }
  .ok.col-2 { left: 503px; }
  .oil-list .continued { padding-left: 9px; }
  .oil-list .continued::before { display: none; }
  .status-icon { position: absolute; left: 974px; width: 166px; height: 166px; }
  .icon-avoid { top: 226px; }
  .icon-ok { top: 456px; }
  .trace-note {
    position: absolute; left: 0; top: 669px;
    width: 871px; height: 102px;
    background: var(--yellow);
  }
  .trace-badge { position: absolute; left: 6px; top: 657px; width: 114px; height: 114px; }
  .trace-text {
    position: absolute; left: 171px; top: 697px;
    font-size: 31px; line-height: 1;
  }
  .trace-text strong { font-weight: 700; }
  .thanks {
    position: absolute; left: 887px; top: 682px;
    width: 300px; text-align: center;
    font-style: italic; font-size: 23px; line-height: 34px;
  }
</style>
</head>
<body>
<main class="card">
  <header class="card-header">
    <h1 class="card-title">DIETARY RESTRICTION CARD</h1>
  </header>

  <h2 class="section-heading heading-avoid">Please <span class="emph-red">I cannot</span> eat any seed oil or processed oil</h2>
  <ul class="oil-list avoid col-1">
    <li>Vegetable oil</li><li>Canola oil</li><li>Soybean oil</li>
  </ul>
  <ul class="oil-list avoid col-2">
    <li>Sunflower oil</li><li>Corn oil</li><li>Cottonseed oil</li>
  </ul>
  <ul class="oil-list avoid col-3">
    <li>Safflower oil</li><li>Peanut oil</li><li>Sesame oil</li>
  </ul>
  <svg class="status-icon icon-avoid" viewBox="0 0 166 166" aria-label="Not allowed" role="img">
    <circle cx="83" cy="83" r="83" fill="#c8000a"/>
    <path d="M53 53 L113 113 M113 53 L53 113" stroke="#ffffff" stroke-width="19" stroke-linecap="round"/>
  </svg>

  <h2 class="section-heading heading-ok">Oils <span style="font-family:'Arimo',Arial,sans-serif;font-weight:700">that are</span> <span class="emph-green">OK</span> <span style="font-family:'Arimo',Arial,sans-serif;font-weight:700">for me to consume</span></h2>
  <ul class="oil-list ok col-1">
    <li>Butter (most preferable)</li><li>Extra virgin olive oil</li><li>Avocado oil</li><li>Coconut oil</li>
  </ul>
  <ul class="oil-list ok col-2">
    <li>Ghee</li><li>Lard</li><li>Any other</li><li class="continued">animal-based fats</li>
  </ul>
  <svg class="status-icon icon-ok" viewBox="0 0 166 166" aria-label="Allowed" role="img">
    <circle cx="83" cy="83" r="83" fill="#3aa535"/>
    <path d="M44 86 L71 113 L123 59" fill="none" stroke="#ffffff" stroke-width="19" stroke-linecap="round" stroke-linejoin="round"/>
  </svg>

  <div class="trace-note"></div>
  <svg class="trace-badge" viewBox="0 0 114 114" aria-label="Notice" role="img">
    <circle cx="57" cy="57" r="57" fill="#ffffff"/>
    <circle cx="57" cy="57" r="48" fill="#ffc90e"/>
    <rect x="50" y="25" width="14" height="42" rx="7" fill="#ffffff"/>
    <circle cx="57" cy="84" r="8" fill="#ffffff"/>
  </svg>
  <p class="trace-text"><strong>Used cookware OK</strong>, no ingredient use.</p>

  <p class="thanks">Thank you for you<br>cooperation</p>
</main>
</body>
</html>
```